Valdarossi’s Artisan Pizzeria Menu Contest

I’m looking for a menu design for a new pizzeria - it’s farm to table type of restaurant - more upscale than a typical pizzeria - white washed wood interior with some industrial accents - I am looking for a creative menu layout using the attached sample menu items -
Valdarossi’s is an artisanal pizzeria with an atmosphere that will make you feel at home for any situation, first date, anniversary, business lunch, boys night out or girls night out with a menu inspired by the idea of a simple honest cooking paired with fresh – quality ingredients. Full service dining experience that is still casual but dedicated to extraordinary hospitality.
While developing the menu we have created a network of amazing farms and purveyors to supply our restaurant with fresh milled 100% California flour for our hand crafted dough, as well as sustainably farmed organic produce, meats and cheeses.
The menu includes classics like the Margherita pizza to daily seasonal specials, fresh salads to rustic small plates including moms meatball recipe to a fresh local burrata with handmade bread. Each dish reflects our passion for sourcing the freshest quality local ingredients.
To compliment the menu, Valdarossi’s serves an extensive wine list with selections focusing on Italian varietals. The cocktail program has been carefully crafted to offer something to entice ever palate and the beer list has unique selections of the world’s finest brewers.
Target Market(s)
25-45 year old men and women
Industry/Entity Type
American Restaurant
Requirements
Must have
- professional tone
Nice to have
- a balance of elegance and industrial (rustic)
Should not have
- photos or playful graphics etc..

```html
<!DOCTYPE html>
<html lang="en">
<head>
<meta charset="utf-8">
<title>Valdarossi’s Artisan Pizzeria — Menu</title>
<link href="https://fonts.googleapis.com/css2?family=Gilda+Display&family=Great+Vibes&display=swap" rel="stylesheet">
<style>
  :root{
    --page:#ffffff;
    --red:#ef4a50;
    --cream:#fdf1dc;
    --beige:#e7d5b3;
    --grey:#a9a6a3;
    --ink:#1b1b1b;
    --serif:"Gilda Display", "Times New Roman", serif;
    --script:"Great Vibes", cursive;
  }
  *{box-sizing:border-box;margin:0;padding:0}
  html,body{width:1200px;height:1200px;overflow:hidden;background:var(--page)}
  .canvas{position:relative;width:1200px;height:1200px;font-family:var(--serif);color:var(--cream)}

  /* cover panel */
  .cover{position:absolute;left:14px;top:131px;width:568px;height:937px;background:var(--red)}
  .damask-strip{position:absolute;top:16px;width:115px;height:905px;background:var(--beige)}
  .damask-strip.left{left:13px}
  .damask-strip.right{left:440px}
  .frame-line{position:absolute;background:var(--grey)}
  .flourish{position:absolute;background:var(--grey);opacity:.55;border-radius:14px}
  .flourish.cream{background:var(--beige);opacity:.9}
  .cover-title{position:absolute;left:0;width:568px;text-align:center;top:100px;font-family:var(--script);font-weight:400;font-size:60px;line-height:66px;color:var(--cream)}
  .cover-list{position:absolute;left:0;width:568px;top:193px;text-align:center;font-size:22px;line-height:31.5px;list-style:none}
  .brand{position:absolute;left:0;width:568px;top:442px;text-align:center;font-size:36px;letter-spacing:1px;color:var(--cream)}
  .divider{position:absolute;left:0;width:568px;display:flex;justify-content:center;align-items:center;gap:8px}
  .divider span{display:block;width:30px;height:2px;background:var(--cream)}
  .divider svg{width:10px;height:12px;color:var(--cream)}
  .tagline{position:absolute;left:0;width:568px;text-align:center;font-size:23px;line-height:32px;top:707px}
  .industry{position:absolute;left:0;width:568px;text-align:center;font-size:19px;top:786px}

  /* dishes panel */
  .dishes{position:absolute;left:618px;top:131px;width:568px;height:937px;background:var(--red)}
  .banner{position:absolute;left:126px;top:21px;width:316px;height:86px}
  .banner-title{position:absolute;left:126px;top:20px;width:316px;text-align:center;font-family:var(--script);font-weight:400;font-size:46px;color:var(--cream)}
  .heading{position:absolute;display:flex;align-items:center;justify-content:center;gap:14px;font-size:21px;font-weight:400;color:var(--cream);white-space:nowrap}
  .heading .flourish{position:static;width:34px;height:16px}
  .menu-list{position:absolute;left:60px;width:450px;list-style:none}
  .item{display:grid;grid-template-columns:12px 102px 48px 1fr;align-items:start;height:15.6px;font-size:11px;line-height:14px}
  .item > span:nth-child(2){white-space:nowrap}
  .menu-list.tall .item{height:16.8px}
  .item svg{width:8px;height:10px;margin-top:2px;color:var(--cream)}
  .item .desc{font-size:7.2px;line-height:7.2px;padding-top:2px}
  .item .desc.fine{font-size:6px;white-space:nowrap}
  .item.double{height:25px}
  .item.double > span:nth-child(2){white-space:normal}
  .small-list{position:absolute;list-style:none}
  .small-list .item{grid-template-columns:14px 103px 40px;height:16.8px}
</style>
</head>
<body>
<svg width="0" height="0" style="position:absolute">
  <symbol id="flame" viewBox="0 0 8 10"><path d="M4 0C5 2.5 7.5 4 7.5 6.5A3.5 3.5 0 0 1 .5 6.5C.5 5 1.5 4 2 3c.3 1 .8 1.6 1.5 1.8C3.5 3 3.2 1.5 4 0z" fill="currentColor"/></symbol>
</svg>

<main class="canvas">

  <section class="cover">
    <div class="damask-strip left" role="img" aria-label="Cream damask pattern strip"></div>
    <div class="damask-strip right" role="img" aria-label="Cream damask pattern strip"></div>

    <div class="frame-line" style="left:152px;top:31px;width:2px;height:348px"></div>
    <div class="frame-line" style="left:152px;top:31px;width:32px;height:2px"></div>
    <div class="frame-line" style="left:416px;top:31px;width:2px;height:348px"></div>
    <div class="frame-line" style="left:386px;top:31px;width:32px;height:2px"></div>
    <div class="flourish" style="left:202px;top:24px;width:166px;height:28px" role="img" aria-label="Grey scroll ornament"></div>

    <div class="frame-line" style="left:152px;top:559px;width:2px;height:349px"></div>
    <div class="frame-line" style="left:152px;top:906px;width:32px;height:2px"></div>
    <div class="frame-line" style="left:416px;top:559px;width:2px;height:349px"></div>
    <div class="frame-line" style="left:386px;top:906px;width:32px;height:2px"></div>
    <div class="flourish" style="left:202px;top:888px;width:166px;height:28px" role="img" aria-label="Grey scroll ornament"></div>

    <div class="flourish cream" style="left:170px;top:124px;width:40px;height:18px" role="img" aria-label="Cream flourish"></div>
    <h1 class="cover-title">Menu</h1>
    <div class="flourish cream" style="left:358px;top:124px;width:40px;height:18px" role="img" aria-label="Cream flourish"></div>

    <ul class="cover-list">
      <li>Pizzas</li><li>&amp;</li><li>Appetizers</li><li>&amp;</li><li>Sandwiches</li>
    </ul>

    <p class="brand">Valdarossi’s</p>

    <div class="divider" style="top:693px"><span></span><svg><use href="#flame"/></svg><span></span></div>
    <p class="tagline">It’s farm to table<br>restaurant</p>
    <div class="divider" style="top:772px"><span></span><svg><use href="#flame"/></svg><span></span></div>
    <p class="industry">American Restaurant</p>
  </section>

  <section class="dishes">
    <div class="frame-line" style="left:132px;top:10px;width:303px;height:3px"></div>
    <div class="frame-line" style="left:132px;top:925px;width:303px;height:3px"></div>
    <div class="frame-line" style="left:12px;top:195px;width:3px;height:546px"></div>
    <div class="frame-line" style="left:556px;top:195px;width:3px;height:546px"></div>
    <div class="flourish" style="left:10px;top:10px;width:62px;height:62px" role="img" aria-label="Corner scroll ornament"></div>
    <div class="flourish" style="left:496px;top:10px;width:62px;height:62px" role="img" aria-label="Corner scroll ornament"></div>
    <div class="flourish" style="left:10px;top:864px;width:62px;height:62px" role="img" aria-label="Corner scroll ornament"></div>
    <div class="flourish" style="left:496px;top:864px;width:62px;height:62px" role="img" aria-label="Corner scroll ornament"></div>

    <svg class="banner" viewBox="0 0 316 86">
      <polygon points="0,42 26,34 26,86 12,72" fill="var(--ink)"/>
      <polygon points="316,42 290,34 290,86 304,72" fill="var(--ink)"/>
      <path d="M24 10 Q158 -6 292 10 L288 66 Q158 50 28 66 Z" fill="var(--ink)" stroke="var(--grey)" stroke-width="2"/>
    </svg>
    <h2 class="banner-title">Dishes</h2>
    <div class="divider" style="left:132px;width:303px;top:105px"><span style="background:var(--grey)"></span><svg style="color:var(--grey)"><use href="#flame"/></svg><span style="background:var(--grey)"></span></div>

    <h3 class="heading" style="left:60px;width:450px;top:102px"><i class="flourish cream" role="img" aria-label="Cream flourish"></i>Appetizers<i class="flourish cream" role="img" aria-label="Cream flourish"></i></h3>
    <ul class="menu-list" style="top:133px">
      <li class="item"><svg><use href="#flame"/></svg><span>Brussels</span><span>$ 10</span><span class="desc">(Pan seared brussel sprouts with a drizzle of balsamic reduction and parm and bread crumbs)</span></li>
      <li class="item"><svg><use href="#flame"/></svg><span>Meatballs</span><span>$ 13</span><span class="desc">(Moms meatballs handmade secret recipe for over 75 years)</span></li>
      <li class="item"><svg><use href="#flame"/></svg><span>Mussels</span><span>$ 15</span><span class="desc">(New Zealand Mussels in a tomato broth)</span></li>
      <li class="item"><svg><use href="#flame"/></svg><span>Romanesco</span><span>$ 11</span><span class="desc">(Flash fried romanesco served atop a spicy aioli)</span></li>
      <li class="item"><svg><use href="#flame"/></svg><span>Chickenwings</span><span>$ 10</span><span class="desc">(Italian fried chicken wings with a kick)</span></li>
      <li class="item"><svg><use href="#flame"/></svg><span>Burrata</span><span>$ 13</span><span class="desc">(Local burrata served with apples grapes and fresh made bread)</span></li>
    </ul>

    <h3 class="heading" style="left:60px;width:450px;top:237px"><i class="flourish cream" role="img" aria-label="Cream flourish"></i>Salads<i class="flourish cream" role="img" aria-label="Cream flourish"></i></h3>
    <ul class="menu-list" style="top:272px">
      <li class="item"><svg><use href="#flame"/></svg><span>Chopped Salad</span><span>$ 13</span><span class="desc">(Lettuce mix with tomato, onions, peppers, pepperoni, chick peas, fresh mozz, italian herb ving)</span></li>
      <li class="item"><svg><use href="#flame"/></svg><span>Caesar Salad</span><span>$ 11</span><span class="desc">(Traditional caesar salad rich and creamy extra shaved parmesan)</span></li>
      <li class="item"><svg><use href="#flame"/></svg><span>Farm Salad</span><span>$ 15</span><span class="desc">(Seasonal farmers market salad)</span></li>
      <li class="item"><svg><use href="#flame"/></svg><span>Grilled Little Gem</span><span>$ 11</span><span class="desc">(Grilled little gems with bacon, tomato, red onions and blue cheese dressing)</span></li>
      <li class="item double"><svg><use href="#flame"/></svg><span>Spinach and<br>Arugula Salad</span><span>$ 12</span><span class="desc">(Spinach and argula, red pepperstossed in a lemon ving and housemade croutons)</span></li>
    </ul>

    <h3 class="heading" style="left:60px;width:450px;top:364px"><i class="flourish cream" role="img" aria-label="Cream flourish"></i>Sandwiches<i class="flourish cream" role="img" aria-label="Cream flourish"></i></h3>
    <ul class="menu-list tall" style="top:398px">
      <li class="item"><svg><use href="#flame"/></svg><span>Italian sub</span><span>$ 13</span><span class="desc">(Prosciutto, salumi, turkey, provolone, lettuce, tomato and herb aioli with spicy gardenia)</span></li>
      <li class="item"><svg><use href="#flame"/></svg><span>Turkey sandwich</span><span>$ 12</span><span class="desc">(housemade bread - turkey, cheddar cheese, butter lettuce, tomato and mustard aioli)</span></li>
      <li class="item"><svg><use href="#flame"/></svg><span>Meatball sub</span><span>$ 13</span><span class="desc">(Moms meatballs melted provolone on a housemade roll)</span></li>
      <li class="item"><svg><use href="#flame"/></svg><span>Verdant burger</span><span>$ 14</span><span class="desc">(Housemade bun - arugula , tomato, onion and a sundried tomato spread)</span></li>
      <li class="item"><svg><use href="#flame"/></svg><span>Chicken sandwich</span><span>$ 13</span><span class="desc">(Fried chicken or chicken breast, provolone, argula, tomato, served with a spicy aioli)</span></li>
    </ul>

    <h3 class="heading" style="left:60px;width:450px;top:491px"><i class="flourish cream" role="img" aria-label="Cream flourish"></i>Pizzas<i class="flourish cream" role="img" aria-label="Cream flourish"></i></h3>
    <ul class="menu-list tall" style="top:525px">
      <li class="item"><svg><use href="#flame"/></svg><span>Margherita</span><span>$ 14</span><span class="desc">(Classic Margherita pizza - Fresh Mozz Tomato Sauce and Basil)</span></li>
      <li class="item"><svg><use href="#flame"/></svg><span>Organic Sausage</span><span>$ 16</span><span class="desc">(Organic Sausage Housemade Red Sauce Mozz hint of fennel)</span></li>
      <li class="item"><svg><use href="#flame"/></svg><span>Pepperoni</span><span>$ 16</span><span class="desc">(Harlow Pepperoni - Housemade Red Sauce Chile flakes and Mozz)</span></li>
      <li class="item"><svg><use href="#flame"/></svg><span>Salumi and Burrata</span><span>$ 17</span><span class="desc">(Salumi dried Red Sauce finished with whipped burrata)</span></li>
      <li class="item"><svg><use href="#flame"/></svg><span>Daily specia</span><span>$ 17</span><span class="desc">............................................................................................</span></li>
      <li class="item"><svg><use href="#flame"/></svg><span>Mushroom</span><span>$ 15</span><span class="desc">(Shaved mushrooms with a Parmesan cream and melted onions)</span></li>
      <li class="item"><svg><use href="#flame"/></svg><span>Prosciutto and egg</span><span>$ 16</span><span class="desc fine">(Parma Prosciutto Parmesan cream with Norvik and gruyere finished with an organic egg)</span></li>
      <li class="item"><svg><use href="#flame"/></svg><span>Quarttro Formaggi</span><span>$ 15</span><span class="desc fine">(Four cheese combination - mozz - fontina - parm cream and gruyere chile flakes and oregano)</span></li>
      <li class="item"><svg><use href="#flame"/></svg><span>Farmers Pizza</span><span>$ 17</span><span class="desc">(Seasonal vegatables cream sauce and a variety of cheese)</span></li>
      <li class="item"><svg><use href="#flame"/></svg><span>Keto friendly</span><span>$ 17</span><span class="desc">(Cauliflower crust, spinach and kale , parm cream sauce)</span></li>
    </ul>

    <h3 class="heading" style="left:60px;width:450px;top:703px"><i class="flourish cream" role="img" aria-label="Cream flourish"></i>Crusts<i class="flourish cream" role="img" aria-label="Cream flourish"></i></h3>
    <ul class="menu-list tall" style="top:737px">
      <li class="item"><svg><use href="#flame"/></svg><span>Traditional</span><span>$</span><span class="desc">(orginal crust you can't miss)</span></li>
      <li class="item"><svg><use href="#flame"/></svg><span>Gluten free</span><span>$ 3</span><span class="desc">(best gluten friendly crust on the west coast)</span></li>
      <li class="item"><svg><use href="#flame"/></svg><span>Cauliflower</span><span>$ 3</span><span class="desc">(Vegans have needs)</span></li>
    </ul>

    <h3 class="heading" style="left:88px;width:150px;top:797px;font-size:17px"><i class="flourish cream" role="img" aria-label="Cream flourish"></i>Dips<i class="flourish cream" role="img" aria-label="Cream flourish"></i></h3>
    <ul class="small-list" style="left:94px;top:827px">
      <li class="item"><svg><use href="#flame"/></svg><span>Ranch</span><span>$ 1</span></li>
      <li class="item"><svg><use href="#flame"/></svg><span>Tomato sauce</span><span>$ 1</span></li>
      <li class="item"><svg><use href="#flame"/></svg><span>spicy dip</span><span>$ 1</span></li>
      <li class="item"><svg><use href="#flame"/></svg><span>blue cheese</span><span>$ 1</span></li>
    </ul>

    <h3 class="heading" style="left:330px;width:150px;top:797px;font-size:17px"><i class="flourish cream" role="img" aria-label="Cream flourish"></i>Daily Soup<i class="flourish cream" role="img" aria-label="Cream flourish"></i></h3>
    <ul class="small-list" style="left:336px;top:824px">
      <li class="item double" style="grid-template-columns:14px 102px 40px;height:32px"><svg><use href="#flame"/></svg><span>Example Tomato<br>bisque</span><span>$ 8</span></li>
    </ul>
  </section>

</main>
</body>
</html>
```